Stufenlos Ratgeber
Zielgruppe
Vermittlung von Aufzügen und Treppenliften.
Aufgabenstellung
Wir benötigen ein Design für ein Treppenlift-Portal.
Das Design sollte sehr anprechend & modern sein sowie möchlichst dazu führen, dass der Nutzer gerne seine Nutzerdaten in einem Formular eingibt, um nähere Informationen zu einem gewünschen Treppenlift zu erhalten.
Da die Seite ebenfalls sehr viele Informationen bereitstellt, ist es notwendig, eine horizontale Navigation mit einer ersten & zweiten Ebene zu integrieren.
Da die Interessentengruppe eher 50plus ist, wäre es schön, wenn bei der Designerstellung die Nutzerfreundlichkeit berücksichtigt werden würde.

```html
<!DOCTYPE html>
<html lang="de">
<head>
<meta charset="utf-8">
<title>Stufenlos Ratgeber</title>
<link href="https://fonts.googleapis.com/css2?family=Ubuntu:wght@400;500;700&family=Noto+Sans:wght@400&display=swap" rel="stylesheet">
<style>
:root{
  --orange:#f07d22;
  --orange-light:#f9a44f;
  --orange-dark:#d9620d;
  --ink:#2b2b2b;
  --text:#333;
  --band:#dcdcdc;
  --footer:#d9d9d9;
  --line:#c8c8c8;
  --white:#fff;
}
*{margin:0;padding:0;box-sizing:border-box}
html,body{width:943px;height:1200px;overflow:hidden}
body{position:relative;background:linear-gradient(#e2e2e2 0,#f4f4f4 110px,#fff 400px,#f7f7f7 1000px);font-family:"Noto Sans",Verdana,sans-serif;color:var(--text)}
.band{position:absolute;left:0;top:135px;width:943px;height:266px;background:var(--band)}
.site-name{position:absolute;left:70px;top:40px;font-family:"Ubuntu",sans-serif;font-size:32px;font-weight:400;color:var(--ink)}
.search{position:absolute;left:645px;top:62px;display:flex;gap:6px}
.search-field{width:161px;height:19px;background:var(--white);border:1px solid #d4d4d4}
.search-btn{width:67px;height:19px;border:1px solid #999;background:linear-gradient(#fff,#e4e4e4);font:11px "Noto Sans",sans-serif;color:#222;display:flex;align-items:center;justify-content:center}
.nav{position:absolute;left:68px;top:94px;width:806px;height:41px;background:linear-gradient(#f4f4f4,#e0e0e0);border:1px solid var(--line);display:flex;font-family:"Ubuntu",sans-serif;font-size:16px;color:#555}
.nav a{display:flex;align-items:center;padding:0 10px;border-right:1px solid var(--line);text-decoration:none;color:inherit}
.nav a.active{color:var(--orange);background:linear-gradient(#fff,#ececec)}
.nav a:last-child{border-right:none}
.hero{position:absolute;left:69px;top:135px;width:805px;height:265px;background:linear-gradient(90deg,#c9c9c9,#f2f2f2 40%,#ebebeb);border:1px solid #c4c4c4;overflow:hidden}
.hero-lift{position:absolute;left:0;top:0;width:180px;height:265px;background:linear-gradient(160deg,#b8a8aa,#d6d6d6 45%,#a9a9a9)}
.hero-couple{position:absolute;right:0;top:0;width:175px;height:265px;background:linear-gradient(150deg,#e6d3bd,#cfcfd6 55%,#eef0f4)}
.hero-title{position:absolute;left:186px;top:10px;font-family:"Ubuntu",sans-serif;font-size:32px;color:#666}
.hero-list{position:absolute;left:190px;top:74px;list-style:none;font-family:"Ubuntu",sans-serif;font-size:21px;color:#555}
.hero-list li{display:flex;align-items:center;gap:12px;height:41px}
.cta{position:absolute;left:420px;top:337px;width:463px;height:51px}
.cta span{position:absolute;left:0;right:0;top:0;height:51px;display:flex;align-items:center;justify-content:center;padding-left:30px;font-family:"Ubuntu",sans-serif;font-size:21px;color:var(--white)}
.card{position:absolute;top:424px;width:257px;height:163px;box-shadow:0 6px 8px -4px rgba(0,0,0,.35)}
.card h3{height:26px;background:linear-gradient(var(--orange-light),var(--orange));color:var(--white);font-family:"Ubuntu",sans-serif;font-weight:500;font-size:16px;text-align:center;line-height:26px;text-shadow:0 1px 1px rgba(0,0,0,.3)}
.card-photo{height:137px;position:relative}
.photo-hall{background:linear-gradient(120deg,#6d6d6d,#9a8f85 45%,#8a6a3c)}
.photo-red{background:linear-gradient(#e8ddd5,#b33a3a 40%,#9c2323)}
.card p{position:absolute;left:0;right:0;bottom:0;height:44px;padding:3px 30px 0 7px;background:rgba(40,40,40,.7);color:var(--white);font-size:10.3px;letter-spacing:.2px;line-height:12.6px;white-space:nowrap}
.content{position:absolute;left:69px;top:624px;width:540px;height:316px;background:var(--white);border:1px solid #e0e0e0;box-shadow:0 8px 8px -6px rgba(0,0,0,.3)}
.content-head{height:33px;background:linear-gradient(var(--orange-light),var(--orange));color:var(--white);font-family:"Ubuntu",sans-serif;font-size:16px;line-height:33px;padding-left:9px;text-shadow:0 1px 1px rgba(0,0,0,.3)}
.content-body{padding:12px 14px 0 10px}
.content h1{font-family:"Ubuntu",sans-serif;font-weight:400;font-size:16px;color:#222}
.content h2{font-family:"Ubuntu",sans-serif;font-weight:500;font-size:12.5px;color:#222;margin:2px 0 10px}
.content p{font-size:12.4px;letter-spacing:.3px;line-height:14.3px;margin-bottom:9px}
.polaroid{position:absolute;left:645px;top:628px;width:222px;height:222px;background:var(--white);transform:rotate(-5deg);box-shadow:0 6px 10px rgba(0,0,0,.35);padding:11px 11px 0}
.polaroid-photo{height:172px;background:linear-gradient(#e6d8c8,#c03c3c 35%,#8e1f1f)}
.polaroid-pin{position:absolute;left:96px;top:-4px;width:22px;height:22px;border-radius:50%;background:radial-gradient(circle at 35% 35%,#fbb56c,var(--orange-dark))}
.polaroid-caption{text-align:center;font-family:"Ubuntu",sans-serif;font-size:14px;color:#555;margin-top:10px}
.footer{position:absolute;left:0;top:1007px;width:943px;height:193px;background:var(--footer);border-top:1px solid #bdbdbd}
.footer p{position:absolute;top:40px;width:262px;font-size:12.4px;letter-spacing:.3px;line-height:14.3px;color:var(--text)}
</style>
</head>
<body>
<div class="band"></div>
<div class="site-name">Stufenlos Ratgeber</div>
<div class="search"><div class="search-field"></div><div class="search-btn">suchen</div></div>

<nav class="nav">
  <a class="active">Startseite</a><a>Lifttypen</a><a>Hersteller</a><a>Fragen &amp; Antworten</a><a>Kontakt</a><a>Impressum</a>
</nav>

<section class="hero">
  <div class="hero-lift" role="img" aria-label="Foto eines Treppenlift-Sitzes"></div>
  <div class="hero-couple" role="img" aria-label="Foto eines lächelnden älteren Paares"></div>
  <div class="hero-title">Sie suchen einen Treppenlift</div>
  <ul class="hero-list">
    <li><svg width="38" height="38" viewBox="0 0 38 38"><circle cx="16" cy="21" r="14" fill="#eee" stroke="#bbb" stroke-width="2"/><path d="M9 20l6 7 15-22" fill="none" stroke="#f07d22" stroke-width="4" stroke-linecap="round" stroke-linejoin="round"/></svg>günstige Treppenlifte</li>
    <li><svg width="38" height="38" viewBox="0 0 38 38"><circle cx="16" cy="21" r="14" fill="#eee" stroke="#bbb" stroke-width="2"/><path d="M9 20l6 7 15-22" fill="none" stroke="#f07d22" stroke-width="4" stroke-linecap="round" stroke-linejoin="round"/></svg>Treppenlifte leasen</li>
    <li><svg width="38" height="38" viewBox="0 0 38 38"><circle cx="16" cy="21" r="14" fill="#eee" stroke="#bbb" stroke-width="2"/><path d="M9 20l6 7 15-22" fill="none" stroke="#f07d22" stroke-width="4" stroke-linecap="round" stroke-linejoin="round"/></svg>gebrauchte Treppenlifte</li>
  </ul>
</section>

<div class="cta">
  <svg width="463" height="58" viewBox="0 0 463 58" style="position:absolute;left:0;top:0">
    <defs><linearGradient id="ctaGrad" x1="0" y1="0" x2="0" y2="1"><stop offset="0" stop-color="#f9a44f"/><stop offset="1" stop-color="#ee7419"/></linearGradient></defs>
    <polygon points="0,25 26,0 463,0 463,51 26,51" fill="url(#ctaGrad)"/>
    <polygon points="453,51 463,51 453,58" fill="#b04e0a"/>
  </svg>
  <span>Ihr kostenloses Angebot anfordern</span>
</div>

<article class="card" style="left:69px">
  <h3>günstige Treppenlifte</h3>
  <div class="card-photo photo-hall" role="img" aria-label="Foto eines Treppenlifts an einer Holztreppe">
    <p>Lorem ipsum dolor sit amet, consectetuer<br>adipiscing elit, sed diam nonummy nibh<br>euismod tincidunt ut laoreet</p>
  </div>
</article>
<article class="card" style="left:343px">
  <h3>Treppenlifte leasen</h3>
  <div class="card-photo photo-red" role="img" aria-label="Foto eines Treppenlifts auf roter Teppichtreppe">
    <p>Lorem ipsum dolor sit amet, consectetuer<br>adipiscing elit, sed diam nonummy nibh<br>euismod tincidunt ut laoreet</p>
  </div>
</article>
<article class="card" style="left:617px">
  <h3>gebrauchte Treppenlifte</h3>
  <div class="card-photo photo-hall" role="img" aria-label="Foto eines Treppenlifts an einer Holztreppe">
    <p>Lorem ipsum dolor sit amet, consectetuer<br>adipiscing elit, sed diam nonummy nibh<br>euismod tincidunt ut laoreet</p>
  </div>
</article>

<main class="content">
  <div class="content-head">Startseite</div>
  <div class="content-body">
    <h1>Überschrift 1</h1>
    <h2>Überschrift 2</h2>
    <p>Lorem ipsum dolor sit amet, consectetuer adipiscing elit, sed diam nonummy nibh euismod tincidunt ut laoreet dolore magna aliquam erat volutpat. Ut wisi enim ad minim veniam, quis nostrud exerci tation ullamcorper suscipit lobortis nisl ut aliquip ex ea commodo consequat. Duis autem vel eum iriure dolor in hendrerit in vulputate velit esse molestie consequat, vel illum dolore eu feugiat nulla facilisis at vero eros et accumsan et iusto odio dignissim qui blandit praesent luptatum zzril delenit augue duis dolore te feugait nulla facilisi.</p>
    <p>Lorem ipsum dolor sit amet, consectetuer adipiscing elit, sed diam nonummy nibh euismod tincidunt ut laoreet dolore magna aliquam erat volutpat. Ut wisi enim ad minim veniam, quis nostrud exerci tation ullamcorper suscipit lobortis nisl ut aliquip ex ea commodo consequat. Duis autem vel eum iriure dolor in hendrerit in vulputate velit esse molestie consequat, vel illum dolore eu feugiat nulla facilisis at vero eros et accumsan et iusto odio dignissim qui blandit praesent luptatum zzril delenit augue duis dolore te feugait nulla facilisi.</p>
  </div>
</main>

<figure class="polaroid">
  <div class="polaroid-photo" role="img" aria-label="Foto eines Treppenlifts auf roter Teppichtreppe"></div>
  <div class="polaroid-pin"></div>
  <figcaption class="polaroid-caption">Stufenlos Ratgeber</figcaption>
</figure>

<footer class="footer">
  <p style="left:70px">Lorem ipsum dolor sit amet, consectetuer adipiscing elit, sed diam nonummy nibh euismod tincidunt ut laoreet dolore magna aliquam erat volutpat. Ut wisi enim ad minim veniam, quis nostrud exerci tation ullamcorper suscipit lobortis nisl ut aliquip ex ea commodo consequat.</p>
  <p style="left:346px">Lorem ipsum dolor sit amet, consectetuer adipiscing elit, sed diam nonummy nibh euismod tincidunt ut laoreet dolore magna aliquam erat volutpat. Ut wisi enim ad minim veniam, quis nostrud exerci tation ullamcorper suscipit lobortis nisl ut aliquip ex ea commodo consequat.</p>
  <p style="left:619px">Lorem ipsum dolor sit amet, consectetuer adipiscing elit, sed diam nonummy nibh euismod tincidunt ut laoreet dolore magna aliquam erat volutpat. Ut wisi enim ad minim veniam, quis nostrud exerci tation ullamcorper suscipit lobortis nisl ut aliquip ex ea commodo consequat.</p>
</footer>
</body>
</html>
```